Meridale Cleaning Services

In need of a business card design suited for a growing cleaning company.

We offer our cleaning and maintenance services to a wide range of clients including but not limited to the following: constuction industry, hospitality, commercial, industrial and domestic

I want the card to be very noticable, i would like people to say 'hey, great card!' when i hand them my card.double sided would be nice

we want our business to come across as exceedingly professional and innovative (different).

a contemporary design is what we have in mind
we want to present an image of a quality business with a high standard of excellence in consistent service.

i just really need a card that persuades top end quality,
our business is very certified and also strives towards environmentaly friendly alternatives
Updates

hey sorry, i have uploaded my company logo design and name
cheers.

hey guys i have added my company logo/name file on my brief page. many thanks

sorry guys a typo in the brief..
address is Tolley Rd. not Tolly Rd
thanks

Industry/Entity Type

Industrial

Requirements
Must have
• company name: meridale cleaning services
operations manager: Colm Varetti
Tel: (02)9373 6204
Fax: (02)8645 7712
Mob: 0438571490

address: 47 Tolly RD Pymble NSW 2073
Postal Adress: PO Box 5832 North Ryde NSW 2113
email: meridaleclean@wexanet.com.au
website: meridalecleaningservices.com.au

```html
<!DOCTYPE html>
<html lang="en">
<head>
<meta charset="utf-8">
<title>Meridale Cleaning Services – Business Card</title>
<link href="https://fonts.googleapis.com/css2?family=Arimo:wght@400;700&display=swap" rel="stylesheet">
<style>
  :root {
    --band-green: #8dc63f;
    --band-blue: #2aa8e0;
    --brand-blue: #1b8fd0;
    --card-white: #ffffff;
    --page-bg: #ffffff;
    --text-dark: #222222;
    --text-grey: #6d6e71;
    --card-edge: #e3e3e3;
  }
  * { box-sizing: border-box; margin: 0; padding: 0; }
  html, body {
    width: 1200px;
    height: 373px;
    overflow: hidden;
    background: var(--page-bg);
    font-family: "Arimo", Arial, sans-serif;
  }
  .canvas {
    position: relative;
    width: 1200px;
    height: 373px;
  }
  .card {
    position: absolute;
    top: 76px;
    width: 538px;
    height: 240px;
    background: var(--card-white);
    border: 1px solid var(--card-edge);
    overflow: hidden;
  }
  .card--front { left: 36px; }
  .card--back { left: 610px; }
  .band {
    position: absolute;
    left: 0;
    width: 100%;
  }
  .band--top { top: 0; height: 24px; background: var(--band-green); }
  .band--bottom { bottom: 0; height: 24px; background: var(--band-blue); }

  .brand {
    position: absolute;
    left: 58px;
    top: 62px;
    display: flex;
    align-items: center;
    gap: 30px;
  }
  .brand__mark {
    width: 118px;
    height: 118px;
    border-radius: 50%;
    background: var(--brand-blue);
  }
  .brand__name {
    color: var(--brand-blue);
    font-weight: 700;
    line-height: 1;
  }
  .brand__name-main {
    display: block;
    font-size: 58px;
    letter-spacing: -1px;
  }
  .brand__name-sub {
    display: block;
    font-size: 19px;
    letter-spacing: 0.5px;
    margin-top: 6px;
    padding-left: 10px;
  }

  .person {
    position: absolute;
    left: 26px;
    top: 44px;
  }
  .person__name {
    color: var(--brand-blue);
    font-size: 24px;
    font-weight: 400;
    line-height: 1.1;
  }
  .person__role {
    color: var(--text-dark);
    font-size: 17px;
    margin-top: 4px;
  }
  .contact {
    position: absolute;
    top: 114px;
    font-size: 15px;
    line-height: 22px;
    color: var(--text-grey);
    list-style: none;
  }
  .contact--phones { left: 26px; }
  .contact--addresses { left: 212px; }
  .contact__label { display: inline-block; width: 36px; }
</style>
</head>
<body>
<main class="canvas">
  <section class="card card--front" aria-label="Card front">
    <div class="band band--top"></div>
    <div class="brand">
      <div class="brand__mark" aria-hidden="true"></div>
      <h1 class="brand__name">
        <span class="brand__name-main">Meridale</span>
        <span class="brand__name-sub">CLEANING SERVICES</span>
      </h1>
    </div>
    <div class="band band--bottom"></div>
  </section>

  <section class="card card--back" aria-label="Card back">
    <div class="band band--top"></div>
    <div class="person">
      <h2 class="person__name">Colm Varetti</h2>
      <p class="person__role">operations manager</p>
    </div>
    <ul class="contact contact--phones">
      <li><span class="contact__label">Tel:</span>(02)9373 6204</li>
      <li><span class="contact__label">Fax:</span>(02)8645 7712</li>
      <li><span class="contact__label">Mob:</span>0438571490</li>
    </ul>
    <ul class="contact contact--addresses">
      <li>47 Tolley Rd Pymble NSW 2073</li>
      <li>PO Box 5832 North Ryde NSW 2113</li>
      <li>meridaleclean@wexanet.com.au</li>
      <li>www.meridalecleaningservices.com.au</li>
    </ul>
    <div class="band band--bottom"></div>
  </section>
</main>
</body>
</html>
```